Criação de Kit com 6 Layouts de Post para Redes Sociais (Facebook, Instagram e etc) para Saúde & Nutrição
" Consultório oftalmológico com ênfase em consultas oftalmológicas, exames complementares e cirurgias oculares "

```html
<!DOCTYPE html>
<html lang="pt-BR">
<head>
<meta charset="UTF-8">
<title>Automedicação — Dra. Helena Vasconi</title>
<link rel="stylesheet" href="https://fonts.googleapis.com/css2?family=Cormorant+Garamond:wght@500&family=Poppins:wght@400;500;700&display=swap">
<style>
  :root {
    --bg-light: #fbf3e6;
    --bg-warm: #efd9b3;
    --bg-deep: #e2c594;
    --gold: #c29350;
    --gold-dark: #9c6f35;
    --brand-brown: #6e5236;
    --card: #ffffff;
    --text: #3c3a38;
    --navy: #1f2b4d;
    --white: #ffffff;
    --sign-face: #f0e2c8;
    --sign-edge: #c9a56f;
    --sign-mark: #5a4028;
  }
  * { margin: 0; padding: 0; box-sizing: border-box; }
  html, body { width: 1200px; height: 1200px; overflow: hidden; }
  body { position: relative; font-family: "Poppins", sans-serif; background: var(--bg-light); }

  .backdrop {
    position: absolute; inset: 0;
    background:
      radial-gradient(ellipse 420px 320px at 170px 120px, rgba(214,176,112,.55), transparent 70%),
      radial-gradient(ellipse 380px 380px at 1100px 1080px, rgba(214,176,112,.55), transparent 70%),
      radial-gradient(ellipse 300px 260px at 1120px 120px, rgba(226,197,148,.5), transparent 70%),
      radial-gradient(ellipse 700px 600px at 600px 560px, var(--bg-light), transparent 80%),
      linear-gradient(160deg, var(--bg-warm), var(--bg-light) 45%, var(--bg-deep));
  }

  .brand {
    position: absolute; top: 218px; left: 0; width: 1200px;
    text-align: center; color: var(--brand-brown);
  }
  .brand-name {
    display: inline-flex; align-items: center; gap: 18px;
    font-family: "Cormorant Garamond", serif; font-weight: 500;
    font-size: 66px; line-height: 1; letter-spacing: 1px;
  }
  .brand-dot { width: 22px; height: 22px; border-radius: 50%; background: var(--gold); }
  .brand-role {
    margin-top: 14px; font-family: "Cormorant Garamond", serif; font-weight: 500;
    font-size: 26px; letter-spacing: 9px; text-transform: uppercase; color: var(--brand-brown);
  }

  .warning-sign { position: absolute; left: 862px; top: 296px; width: 150px; height: 150px; }

  .info-card {
    position: absolute; left: 360px; top: 408px; width: 547px; height: 384px;
    background: var(--card); border-radius: 40px;
    box-shadow: 0 20px 50px rgba(150,110,60,.18);
    text-align: center; padding: 70px 24px 0;
  }
  .info-title {
    font-weight: 700; font-size: 44px; line-height: 1;
    color: var(--gold);
    background: linear-gradient(90deg, var(--gold-dark), var(--gold) 50%, var(--gold-dark));
    -webkit-background-clip: text; background-clip: text; -webkit-text-fill-color: transparent;
  }
  .info-text {
    margin-top: 34px; font-size: 21.5px; line-height: 31px; color: var(--text);
  }

  .contact-button {
    position: absolute; left: 468px; top: 810px; width: 272px; height: 56px;
    background: var(--navy); border-radius: 28px;
    display: flex; align-items: center; gap: 16px; padding-left: 14px;
    color: var(--white); font-size: 24px; font-weight: 400;
  }
  .contact-button svg { width: 34px; height: 34px; }

  .pills-visual {
    position: absolute; left: 225px; top: 705px; width: 430px; height: 425px;
    border-radius: 46% 54% 40% 60% / 45% 40% 60% 55%;
    background:
      radial-gradient(ellipse 130px 170px at 130px 150px, rgba(92,48,22,.85), transparent 75%),
      radial-gradient(ellipse 220px 140px at 240px 330px, rgba(178,48,48,.55), transparent 75%),
      radial-gradient(ellipse 260px 200px at 230px 300px, rgba(240,236,228,.9), transparent 80%);
  }
</style>
</head>
<body>
  <div class="backdrop" role="img" aria-label="Fundo bege desfocado com placas de aviso ao fundo"></div>

  <header class="brand">
    <div class="brand-name"><span class="brand-dot"></span>Dra. Helena Vasconi</div>
    <div class="brand-role">Oftalmologista</div>
  </header>

  <svg class="warning-sign" viewBox="0 0 150 150" aria-hidden="true">
    <path d="M75 14 Q82 14 86 21 L140 118 Q144 128 134 132 L16 132 Q6 128 10 118 L64 21 Q68 14 75 14 Z"
          fill="var(--sign-face)" stroke="var(--sign-edge)" stroke-width="8" stroke-linejoin="round"/>
    <rect x="68" y="50" width="14" height="46" rx="7" fill="var(--sign-mark)"/>
    <circle cx="75" cy="111" r="8" fill="var(--sign-mark)"/>
  </svg>

  <section class="info-card">
    <h1 class="info-title">Automedicação</h1>
    <p class="info-text">
      O uso indiscriminado de colírios e outros<br>
      medicamentos sem orientação médica<br>
      pode levar a sérios problemas oculares,<br>
      como glaucoma, catarata, lesões na<br>
      córnea e até mesmo perda de visão.
    </p>
  </section>

  <div class="pills-visual" role="img" aria-label="Frasco âmbar tombado com cápsulas e comprimidos coloridos espalhados"></div>

  <div class="contact-button">
    <svg viewBox="0 0 34 34" aria-hidden="true">
      <circle cx="17" cy="17" r="17" fill="var(--white)"/>
      <path d="M14 10 L21 17 L14 24" fill="none" stroke="var(--navy)" stroke-width="3.5" stroke-linecap="round" stroke-linejoin="round"/>
    </svg>
    Fale conosco
  </div>
</body>
</html>
```